Business Card Design Project for - The Pellowick Greenworks Company Ltd. We are a Landscape and garden

I would like designer to use all special glosses etc so i can have a professional looking business card. The theme of the business card can reflect that of the Logo attached by MarkQuarry or your own unique ideas.. please feel free to go wild as i hope i can select a winner i like - my budget will be committed so please get involved. Good luck and thank you Lyndon

Target Market(s)

Must look Professional

General Public and Businesses including Councils, Local Government, Hospitals, Hotels, Professionals and Professional Sports People.

Industry/Entity Type

Landscape Gardening

Contact Information for Business Card

The Pellowick Greenworks Company Ltd

Mr L.R Ashcombe
Head Office - Quayfront Park Manchester
t. 0772 408 916
e. info@pellowickgreenworks.co.uk
w. www.pellowickgreenworks.co.uk

Facebook - https://www.friendpage-example.com/ThePellowickGreenworksCompany/
Twitter - https://chirpline-example.com/ThePruningCart
Instagram - https://www.snapgrid-example.com/thepellowickgreenworkscompany/?hl=en
Google+ - https://circles.searchhub-example.com/u/0/208473950162438571093
Yelp - https://www.reviewnook-example.co.uk/biz/the-pellowick-greenworks-company-manchester-4

Font styles to use
Serif
Script
Other font styles liked:
• I don't have much of an idea of font types sorry

Colors

Designer to choose colors to be used in the design.

Requirements
Must have
• A Professional look and Design
• Special effects with gloss and fading of colours possibly..
• Front and back design
Nice to have
• All special features with effects and gloss etc

```html
<!DOCTYPE html>
<html lang="en">
<head>
<meta charset="utf-8">
<title>The Pellowick Greenworks Company Ltd — Business Card</title>
<link rel="stylesheet" href="https://fonts.googleapis.com/css2?family=Cinzel:wght@400&family=Open+Sans:wght@400;600&display=swap">
<style>
  :root{
    --page:#e9eae6;
    --card:#ffffff;
    --card-shade:#eceded;
    --navy-dark:#0d2a3f;
    --navy:#1f4a63;
    --green:#8cc63f;
    --green-light:#c6e27a;
    --green-deep:#3fae49;
    --brand-grey:#9a9c9e;
    --ink-light:#ffffff;
    --ink-soft:#d9e4ea;
  }
  *{box-sizing:border-box;margin:0;padding:0}
  html,body{width:1200px;height:1023px;overflow:hidden}
  body{background:var(--page);font-family:"Open Sans",Arial,sans-serif;position:relative}
  .card{
    position:absolute;left:250px;width:700px;height:400px;border-radius:18px;overflow:hidden;
    background:linear-gradient(135deg,var(--card) 0%,var(--card) 55%,var(--card-shade) 100%);
    box-shadow:0 6px 18px rgba(0,0,0,.18);
  }
  .card--contact{top:70px}
  .card--front{top:553px}
  .card__art{position:absolute;inset:0}
  .contact{position:absolute;left:42px;top:46px;color:var(--ink-light)}
  .contact__name{font-size:30px;font-weight:400;letter-spacing:.3px}
  .contact__title{font-size:18px;color:var(--ink-soft);margin-top:2px}
  .contact__list{list-style:none;margin-top:26px}
  .contact__list li{display:flex;align-items:center;gap:10px;font-size:15px;line-height:26px}
  .contact__list svg{width:14px;height:14px;flex:none}
  .social{list-style:none;margin-top:18px}
  .social li{display:flex;align-items:center;gap:10px;font-size:13px;line-height:22px;color:var(--ink-soft)}
  .social__dot{width:12px;height:12px;border-radius:50%;background:var(--green-light);flex:none}
  .brand{position:absolute;display:flex;align-items:center;gap:16px}
  .brand__mark{width:54px;height:54px;border-radius:50%;background:linear-gradient(135deg,var(--green-light),var(--green-deep));flex:none}
  .brand__name{font-family:"Cinzel",Georgia,serif;font-weight:400;color:var(--brand-grey);font-size:24px;line-height:30px;letter-spacing:1px}
  .card--contact .brand{left:420px;top:70px}
  .card--front .brand{left:50%;top:50%;transform:translate(-50%,-50%)}
  .card--front .brand__name{font-size:30px;line-height:38px}
  .card--front .brand__mark{width:70px;height:70px}
</style>
</head>
<body>

<section class="card card--contact" aria-label="Business card, contact side">
  <svg class="card__art" viewBox="0 0 700 400" preserveAspectRatio="none" aria-hidden="true">
    <defs>
      <linearGradient id="navyFade" x1="0" y1="0" x2="1" y2="1">
        <stop offset="0" stop-color="#123349"/>
        <stop offset=".55" stop-color="#2a5670"/>
        <stop offset="1" stop-color="#0d2a3f"/>
      </linearGradient>
      <linearGradient id="swoosh" x1="0" y1="0" x2="1" y2="1">
        <stop offset="0" stop-color="#8cc63f"/>
        <stop offset="1" stop-color="#d4ea95"/>
      </linearGradient>
      <linearGradient id="gloss" x1="0" y1="0" x2="0" y2="1">
        <stop offset="0" stop-color="#fff" stop-opacity=".16"/>
        <stop offset=".5" stop-color="#fff" stop-opacity="0"/>
      </linearGradient>
    </defs>
    <path d="M268,0 C368,120 528,300 700,372 V400 H640 C520,300 380,120 290,0 Z" fill="url(#swoosh)"/>
    <path d="M0,0 H290 C380,120 520,300 640,400 H0 Z" fill="url(#navyFade)"/>
    <path d="M0,0 H290 C330,55 360,95 390,130 C260,170 120,160 0,120 Z" fill="url(#gloss)"/>
  </svg>

  <div class="contact">
    <h1 class="contact__name">Mr L.R Ashcombe</h1>
    <p class="contact__title">Title</p>
    <ul class="contact__list">
      <li><svg viewBox="0 0 16 16"><path d="M3 1l3 3-2 2c1 2 3 4 6 6l2-2 3 3-2 2C7 15 1 9 1 3z" fill="#8cc63f"/></svg>0772 408 916</li>
      <li><svg viewBox="0 0 16 16"><rect x="1" y="3" width="14" height="10" fill="#8cc63f"/><path d="M1 3l7 6 7-6" fill="none" stroke="#1f4a63" stroke-width="1.4"/></svg>info@pellowickgreenworks.co.uk</li>
      <li><svg viewBox="0 0 16 16"><circle cx="8" cy="8" r="6.5" fill="none" stroke="#8cc63f" stroke-width="1.6"/><path d="M1.5 8h13M8 1.5c-3 3-3 10 0 13M8 1.5c3 3 3 10 0 13" fill="none" stroke="#8cc63f" stroke-width="1.2"/></svg>www.pellowickgreenworks.co.uk</li>
    </ul>
    <ul class="social">
      <li><span class="social__dot"></span>/ThePellowickGreenworksCompany</li>
      <li><span class="social__dot"></span>/ThePruningCart</li>
      <li><span class="social__dot"></span>/thepellowickgreenworkscompany</li>
      <li><span class="social__dot"></span>/thepellowickgreenworkscompany</li>
      <li><span class="social__dot"></span>/thepellowickgreenworkscompany</li>
    </ul>
  </div>

  <div class="brand">
    <span class="brand__mark"></span>
    <p class="brand__name">The Pellowick<br>Greenworks Company Ltd</p>
  </div>
</section>

<section class="card card--front" aria-label="Business card, front side">
  <div class="brand">
    <span class="brand__mark"></span>
    <p class="brand__name">The Pellowick<br>Greenworks Company Ltd</p>
  </div>
</section>

</body>
</html>
```